Animal Hospital Business Cards

Make a business card look like the attached example

*Use the same blue/black coloring
*Brisket Hollow Animal Hospital (instead of pet home rounds)
*Emergency Services (instead of tamsin creek clinic)
*House Calls (instead of open 7 days by appointment)
*Change address to 278 Brisket Hollow Rd Fernmoor Vale, ZN 45263
*Open 7 days a week (instead of emergency service)
*Add the website www.briskethollowanimalhospital.example

On the back...
*instead of the text outlined in red, just white
*instead of the light blue, try your best to make it just like the blue and black on the front side of the card
*Delete "designed and printed by 9 whiskers inc, www.pressfeline.example

Requirements
Must have
• look just like the attached example with requested edits/changes

```html
<!DOCTYPE html>
<html lang="en">
<head>
<meta charset="utf-8">
<title>Brisket Hollow Animal Hospital – Business Cards</title>
<link rel="stylesheet" href="https://fonts.googleapis.com/css2?family=Open+Sans:wght@400;600;700;800&family=Tinos:wght@700&display=swap">
<style>
  :root {
    --teal: #17708a;
    --teal-dark: #0f5468;
    --teal-light: #2a8fa9;
    --teal-text: #1a86a3;
    --ink: #111111;
    --paper: #ffffff;
    --red: #c4161c;
    --stage: #e9ecee;
    --mon: #8e1f73; --tue: #f07a3c; --wed: #2c7fc9; --thu: #d8322b;
    --fri: #f2c51c; --sat: #f39bc4; --sun: #1f7a2d;
  }
  * { box-sizing: border-box; margin: 0; padding: 0; }
  html, body { width: 1200px; height: 900px; overflow: hidden; }
  body {
    background: var(--stage);
    font-family: "Open Sans", Arial, sans-serif;
    display: flex; flex-direction: column; align-items: center; justify-content: center;
    gap: 28px;
  }
  .card {
    position: relative; width: 680px; height: 388px;
    background: var(--paper); border-radius: 26px; overflow: hidden;
    box-shadow: 0 6px 18px rgba(0,0,0,.18);
  }
  .card-bands { position: absolute; inset: 0; width: 100%; height: 100%; }

  /* Front */
  .front-title {
    position: absolute; top: 12px; right: 36px;
    color: var(--paper); font-weight: 700; font-size: 31px; letter-spacing: .2px;
  }
  .front-hours {
    position: absolute; bottom: 16px; left: 44px;
    color: var(--paper); font-weight: 700; font-size: 33px;
  }
  .center-block {
    position: absolute; top: 92px; left: 150px; right: 130px; text-align: center; color: var(--ink);
  }
  .vet-name {
    font-family: "Tinos", "Times New Roman", serif; font-weight: 700; font-size: 30px; line-height: 1.2;
  }
  .species {
    margin-top: 6px;
    font-family: "Tinos", "Times New Roman", serif; font-weight: 700; font-size: 21px;
  }
  .clinic-mark {
    margin-top: 8px;
    display: flex; justify-content: center; align-items: center; gap: 7px;
    font-weight: 700; font-size: 13px;
  }
  .clinic-mark .dot { width: 12px; height: 12px; border-radius: 50%; background: var(--red); }
  .phone { margin-top: 4px; color: var(--red); font-weight: 700; font-size: 27px; }
  .website { margin-top: 2px; font-weight: 700; font-size: 14px; }
  .side-left { position: absolute; top: 98px; left: 26px; color: var(--ink); }
  .side-right { position: absolute; top: 226px; right: 26px; color: var(--ink); text-align: center; }
  .side-heading { font-weight: 700; font-size: 16px; line-height: 1.1; }
  .side-note { font-size: 11.5px; line-height: 1.3; margin-top: 4px; }

  /* Back */
  .back-head {
    position: absolute; top: 8px; right: 40px; text-align right; text-align: right; color: var(--paper);
  }
  .back-title { font-weight: 700; font-size: 29px; line-height: 1.15; }
  .back-sub { font-size: 15px; line-height: 1.3; }
  .form { position: absolute; left: 38px; right: 38px; top: 128px; color: var(--teal-text); font-weight: 600; font-size: 19px; }
  .form-row { display: flex; align-items: flex-end; gap: 8px; }
  .blank { flex: 1; border-bottom: 2px solid var(--ink); height: 20px; }
  .blank.short { flex: 0 0 150px; }
  .ampm { display: flex; flex-direction: column; font-size: 15px; line-height: 1.05; margin-bottom: -6px; }
  .days { display: flex; justify-content: space-between; margin: 34px 0 40px; }
  .day {
    width: 72px; height: 30px; border-radius: 15px;
    display: flex; align-items: center; justify-content: center;
    font-size: 13px; font-weight: 600; color: var(--ink);
  }
  .mon { background: var(--mon); } .tue { background: var(--tue); } .wed { background: var(--wed); }
  .thu { background: var(--thu); } .fri { background: var(--fri); } .sat { background: var(--sat); }
  .sun { background: var(--sun); }
</style>
</head>
<body>

<section class="card card-front" aria-label="Business card front">
  <svg class="card-bands" viewBox="0 0 680 388" preserveAspectRatio="none" aria-hidden="true">
    <defs>
      <linearGradient id="tealBand" x1="0" y1="0" x2="0" y2="1">
        <stop offset="0" stop-color="#2a8fa9"/><stop offset="1" stop-color="#0f5468"/>
      </linearGradient>
    </defs>
    <rect x="0" y="0" width="680" height="66" fill="url(#tealBand)"/>
    <polygon points="0,62 330,62 290,82 0,82" fill="#111"/>
    <rect x="0" y="320" width="680" height="68" fill="url(#tealBand)"/>
    <polygon points="0,304 250,304 290,322 0,322" fill="#111"/>
  </svg>
  <h1 class="front-title">Brisket Hollow Animal Hospital</h1>
  <div class="center-block">
    <p class="vet-name">Marlowe J. Penhallow, DVM</p>
    <p class="species">•Cats •Dogs •Birds •Exotics</p>
    <p class="clinic-mark"><span class="dot"></span>Brisket Hollow</p>
    <p class="phone">(555) 014-2290</p>
    <p class="website">www.briskethollowanimalhospital.example</p>
  </div>
  <div class="side-left">
    <p class="side-heading">Emergency<br>Services</p>
    <p class="side-note">278 Brisket Hollow Rd<br>Fernmoor Vale, ZN 45263</p>
  </div>
  <div class="side-right">
    <p class="side-heading">House<br>Calls</p>
    <p class="side-note">30 Years<br>of Experience</p>
  </div>
  <p class="front-hours">Open 7 days a week</p>
</section>

<section class="card card-back" aria-label="Business card back">
  <svg class="card-bands" viewBox="0 0 680 388" preserveAspectRatio="none" aria-hidden="true">
    <defs>
      <linearGradient id="tealBandBack" x1="0" y1="0" x2="0" y2="1">
        <stop offset="0" stop-color="#2a8fa9"/><stop offset="1" stop-color="#0f5468"/>
      </linearGradient>
    </defs>
    <rect x="0" y="0" width="680" height="100" fill="url(#tealBandBack)"/>
    <polygon points="0,0 120,0 300,100 0,100" fill="#111"/>
    <polygon points="0,0 90,0 250,100 0,100" fill="#ffffff"/>
    <rect x="0" y="100" width="680" height="6" fill="#e6e9ea"/>
  </svg>
  <div class="back-head">
    <h2 class="back-title">Veterinary Appointment</h2>
    <p class="back-sub">Marlowe J. Penhallow, DVM</p>
    <p class="back-sub">555.014.2290</p>
  </div>
  <div class="form">
    <div class="form-row"><span>Your appointment for</span><span class="blank"></span></div>
    <div class="days">
      <span class="day mon">Mon</span><span class="day tue">Tues</span><span class="day wed">Wed</span>
      <span class="day thu">Thur</span><span class="day fri">Fri</span><span class="day sat">Sat</span>
      <span class="day sun">Sun</span>
    </div>
    <div class="form-row">
      <span>Date</span><span class="blank"></span>
      <span>Time</span><span class="blank short"></span>
      <span class="ampm"><span>AM</span><span>PM</span></span>
      <span>is on</span>
    </div>
  </div>
</section>

</body>
</html>
```